Ned Halvorsen Executive Coach Business Card Design

I need a new card design for my Executive Coaching practice. I am a Clinical Psychotherapist and Executive Coach. I help my clients get the most out of life by developing their personal and professional skills and abilities.

I work with senior executives. My design needs to be high end. I am thinking gloss on the front. I am also thinking contemporary. I am going to use a black, grey and red colour scheme on the the website. I am thinking grey with black and red accents. I would also like a water mark included on the card.

Target Market(s)

Senior Executives In major Companies

Industry/Entity Type

Business

Contact Information for Business Card

On the front

Ned Halvorsen
Clinical Psychotherapist and Executive Coach
For Personal and Professional Success

On the Back

Tarwin office
87 Tarwin Vale Road Tarwin

North Sydney Office
Suite 309 / 41 Lathom Street North Sydney

Pellington Street Office
Suite 512 / 218 Pellington Street Sydney CBD

Phone 02 95817364
Email ned@nedhalvorsen.com.au

Requirements
Must have
• Friendly but professional
Water Mark
Gloss Front

```html
<!DOCTYPE html>
<html lang="en">
<head>
<meta charset="utf-8">
<title>Ned Halvorsen – Business Card</title>
<link rel="stylesheet" href="https://fonts.googleapis.com/css2?family=Montserrat:wght@300;400;500&family=Arimo:wght@400&display=swap">
<style>
  :root {
    --canvas: #e4e2df;
    --card: #eef0ef;
    --card-edge: #dfe2e1;
    --ink: #1c1c1c;
    --ink-soft: #3a3a3a;
    --accent-red: #8e2f38;
    --watermark: #f8f9f9;
    --watermark-shade: #d3d6d5;
  }
  * { box-sizing: border-box; margin: 0; padding: 0; }
  html, body {
    width: 1200px; height: 1000px; overflow: hidden;
    background: var(--canvas);
  }
  .canvas {
    position: relative; width: 1200px; height: 1000px;
    display: flex; flex-direction: column; align-items: center; justify-content: center; gap: 40px;
  }
  .card {
    position: relative; width: 760px; height: 434px; overflow: hidden;
    background: linear-gradient(135deg, #f6f7f7 0%, var(--card) 45%, var(--card-edge) 100%);
    box-shadow: 0 10px 28px rgba(0,0,0,.16), 0 2px 4px rgba(0,0,0,.08);
    font-family: "Montserrat", sans-serif; color: var(--ink);
  }
  .card-texture {
    position: absolute; inset: 0;
    background: linear-gradient(150deg, rgba(255,255,255,.55) 0%, rgba(255,255,255,0) 40%, rgba(210,214,213,.35) 100%);
  }
  .front-name {
    position: absolute; left: 96px; top: 58px;
    font-weight: 300; font-size: 40px; letter-spacing: .5px; text-transform: uppercase;
  }
  .front-title {
    position: absolute; left: 96px; top: 112px;
    font-family: "Arimo", sans-serif; font-size: 16px; color: var(--ink-soft);
  }
  .front-rule {
    position: absolute; left: 450px; right: 0; top: 134px; height: 1px;
    background: var(--accent-red);
  }
  .front-rule-lead {
    position: absolute; left: 84px; width: 10px; top: 106px; height: 1px;
    background: var(--accent-red);
  }
  .front-tagline {
    position: absolute; left: 96px; bottom: 52px;
    font-weight: 300; font-size: 26px; letter-spacing: .6px; text-transform: uppercase;
  }
  .watermark {
    position: absolute; left: 0; right: 40px; top: 40px; text-align: right;
    color: var(--watermark); text-shadow: 1px 1px 1px var(--watermark-shade);
    text-transform: uppercase;
  }
  .watermark-name { font-weight: 300; font-size: 64px; letter-spacing: 1px; line-height: 1; }
  .watermark-title { font-size: 24px; font-weight: 400; margin-top: 6px; text-transform: none; }
  .contact {
    position: absolute; left: 62px; top: 190px; font-size: 15px; color: var(--ink-soft);
  }
  .contact-line { display: flex; align-items: center; gap: 10px; height: 22px; }
  .contact-line svg { width: 15px; height: 15px; fill: var(--ink-soft); }
  .back-rule {
    position: absolute; left: 62px; right: 0; top: 250px; height: 1px; background: var(--accent-red);
  }
  .offices {
    position: absolute; left: 62px; top: 266px; list-style: none;
    font-size: 16px; line-height: 26px; color: var(--ink);
  }
</style>
</head>
<body>
<main class="canvas">
  <section class="card card-front" aria-label="Card front">
    <div class="card-texture" role="img" aria-label="Fine diagonal pinstripe texture on glossy grey stock"></div>
    <span class="front-rule-lead"></span>
    <h1 class="front-name">Ned Halvorsen</h1>
    <p class="front-title">Clinical Psychotherapist and Executive Coach</p>
    <span class="front-rule"></span>
    <p class="front-tagline">For Personal and Professional Success</p>
  </section>

  <section class="card card-back" aria-label="Card back">
    <div class="watermark" aria-hidden="true">
      <div class="watermark-name">Ned Halvorsen</div>
      <div class="watermark-title">Clinical Psychotherapist and Executive Coach</div>
    </div>
    <div class="contact">
      <p class="contact-line">
        <svg viewBox="0 0 16 16" aria-hidden="true"><path d="M3 2h3l1 3-2 1.5a9 9 0 0 0 4.5 4.5L11 9l3 1v3a1 1 0 0 1-1 1C7 14 2 9 2 3a1 1 0 0 1 1-1z"/></svg>
        02 95 817 364
      </p>
      <p class="contact-line">
        <svg viewBox="0 0 16 16" aria-hidden="true"><path d="M1 3h14v10H1z M2 4.2v.6l6 4 6-4v-.6z" fill-rule="evenodd"/></svg>
        ned@nedhalvorsen.com.au
      </p>
    </div>
    <span class="back-rule"></span>
    <ul class="offices">
      <li>Tarwin office: 87 Tarwin Vale Road Tarwin North Sydney</li>
      <li>Office Suite: 309 / 41 Lathom Street North Sydney Pellington Street</li>
      <li>Office Suite: 512 / 218 Pellington Street Sydney CBD</li>
    </ul>
  </section>
</main>
</body>
</html>
```